Skin care manufacturer looking for packaging design for new skin care brand.

We need a design and logo for a skin care brand to be sold at retail stores and online in the United States and Europe. The design will be for 1.7oz - 2oz serums that will not have a retail box. The name of the brand is Orvia Lune and should be a luxurious brand that is approachable. The brand will consist of 4 face serums - Vitamin C, Collagen, Retinol and Hyaluronic Acid that all contain Dead Sea Minerals. Images shown are for inspiration only. Color of bottles can be varied based on design and bottles can be screen printed or labeled.

```html
<!DOCTYPE html>
<html lang="en">
<head>
<meta charset="utf-8">
<title>Orvia Lune Serum Collection</title>
<link href="https://fonts.googleapis.com/css2?family=Lato:wght@400;700&display=swap" rel="stylesheet">
<style>
  :root {
    --canvas: #ffffff;
    --silver: #d3d6dc;
    --silver-line: rgba(220, 223, 230, 0.85);
    --retinol: #2b2a92;
    --vitamin-c: #7b3c20;
    --collagen: #8c1f6f;
    --hyaluronic: #1f6d6a;
  }
  * { box-sizing: border-box; margin: 0; padding: 0; }
  html, body { width: 1200px; height: 900px; overflow: hidden; background: var(--canvas); }
  body { font-family: "Lato", sans-serif; }

  .collection {
    position: relative;
    width: 1200px;
    height: 900px;
    display: flex;
    justify-content: center;
    align-items: flex-end;
    gap: 36px;
    padding-bottom: 90px;
  }
  .bottle { width: 240px; display: flex; flex-direction: column; align-items: center; }
  .dropper { width: 150px; height: 240px; display: block; margin-bottom: -2px; }

  .bottle-body {
    width: 240px;
    height: 440px;
    border-radius: 100px 100px 26px 26px;
    padding: 70px 20px 22px;
    display: flex;
    flex-direction: column;
    align-items: center;
    color: var(--silver);
  }
  .bottle--retinol .bottle-body { background: linear-gradient(90deg, #22217a, var(--retinol) 45%, #3a39a6); }
  .bottle--vitamin-c .bottle-body { background: linear-gradient(90deg, #64301a, var(--vitamin-c) 45%, #8d4a2c); }
  .bottle--collagen .bottle-body { background: linear-gradient(90deg, #741a5c, var(--collagen) 45%, #a03480); }
  .bottle--hyaluronic .bottle-body { background: linear-gradient(90deg, #185a57, var(--hyaluronic) 45%, #2c817c); }

  .brand-name {
    font-size: 24px;
    font-weight: 400;
    letter-spacing: 1px;
    text-transform: uppercase;
    color: var(--silver);
    margin-bottom: 22px;
  }
  .label-frame {
    width: 100%;
    border: 1.5px solid var(--silver-line);
    text-align: center;
    flex: 1;
    display: flex;
    flex-direction: column;
  }
  .label-section { border-bottom: 1.5px solid var(--silver-line); padding: 10px 6px; }
  .label-section:last-child { border-bottom: none; }
  .headline { font-size: 16px; letter-spacing: 1px; text-transform: uppercase; line-height: 1.2; padding: 16px 6px 14px; }
  .headline-top { font-size: 14px; }
  .descriptor { font-size: 10.5px; font-weight: 700; padding: 8px 4px; white-space: nowrap; }
  .product { flex: 1; display: flex; flex-direction: column; justify-content: center; }
  .product-name { font-size: 30px; line-height: 1.05; letter-spacing: 0.5px; text-transform: uppercase; }
  .product-name--long { font-size: 25px; letter-spacing: 0; line-height: 1.15; }
  .product-note { font-size: 10px; font-weight: 700; margin-top: 6px; }
  .volume { font-size: 10.5px; font-weight: 700; padding: 10px 4px; }
</style>
</head>
<body>
<main class="collection">
  <svg width="0" height="0" aria-hidden="true" style="position:absolute">
    <defs>
      <linearGradient id="cap-shine" x1="0" x2="1">
        <stop offset="0" stop-color="#050506"/>
        <stop offset="0.25" stop-color="#3a3a40"/>
        <stop offset="0.4" stop-color="#0c0c0e"/>
        <stop offset="0.75" stop-color="#1e1e22"/>
        <stop offset="1" stop-color="#050506"/>
      </linearGradient>
    </defs>
  </svg>

  <article class="bottle bottle--retinol">
    <svg class="dropper" viewBox="0 0 150 240" aria-hidden="true">
      <rect x="50" y="0" width="50" height="115" rx="25" fill="url(#cap-shine)"/>
      <rect x="12" y="105" width="126" height="135" rx="8" fill="url(#cap-shine)"/>
      <rect x="8" y="185" width="134" height="8" fill="#3a3a40"/>
      <rect x="8" y="205" width="134" height="6" fill="#3a3a40"/>
    </svg>
    <div class="bottle-body">
      <p class="brand-name">Orvia Lune</p>
      <div class="label-frame">
        <div class="label-section headline"><span class="headline-top">Anti-Aging</span><br>Facial Serum</div>
        <div class="label-section descriptor">Anti-Aging &amp; Smoothing Treatment</div>
        <div class="label-section product"><p class="product-name">Retinol</p><p class="product-note">With Dead Sea Minerals</p></div>
        <div class="label-section volume">1.7 oz / 50 ml</div>
      </div>
    </div>
  </article>

  <article class="bottle bottle--vitamin-c">
    <svg class="dropper" viewBox="0 0 150 240" aria-hidden="true">
      <rect x="50" y="0" width="50" height="115" rx="25" fill="url(#cap-shine)"/>
      <rect x="12" y="105" width="126" height="135" rx="8" fill="url(#cap-shine)"/>
      <rect x="8" y="185" width="134" height="8" fill="#3a3a40"/>
      <rect x="8" y="205" width="134" height="6" fill="#3a3a40"/>
    </svg>
    <div class="bottle-body">
      <p class="brand-name">Orvia Lune</p>
      <div class="label-frame">
        <div class="label-section headline"><span class="headline-top">Anti-Aging</span><br>Facial Serum</div>
        <div class="label-section descriptor">Brightening &amp; Antioxidant Defense</div>
        <div class="label-section product"><p class="product-name">Vitamin C</p><p class="product-note">With Dead Sea Minerals</p></div>
        <div class="label-section volume">1.7 oz / 50 ml</div>
      </div>
    </div>
  </article>

  <article class="bottle bottle--collagen">
    <svg class="dropper" viewBox="0 0 150 240" aria-hidden="true">
      <rect x="50" y="0" width="50" height="115" rx="25" fill="url(#cap-shine)"/>
      <rect x="12" y="105" width="126" height="135" rx="8" fill="url(#cap-shine)"/>
      <rect x="8" y="185" width="134" height="8" fill="#3a3a40"/>
      <rect x="8" y="205" width="134" height="6" fill="#3a3a40"/>
    </svg>
    <div class="bottle-body">
      <p class="brand-name">Orvia Lune</p>
      <div class="label-frame">
        <div class="label-section headline"><span class="headline-top">Anti-Aging</span><br>Facial Serum</div>
        <div class="label-section descriptor">Firming &amp; Revitalizing Serum</div>
        <div class="label-section product"><p class="product-name">Collagen</p><p class="product-note">With Dead Sea Minerals</p></div>
        <div class="label-section volume">1.7 oz / 50 ml</div>
      </div>
    </div>
  </article>

  <article class="bottle bottle--hyaluronic">
    <svg class="dropper" viewBox="0 0 150 240" aria-hidden="true">
      <rect x="50" y="0" width="50" height="115" rx="25" fill="url(#cap-shine)"/>
      <rect x="12" y="105" width="126" height="135" rx="8" fill="url(#cap-shine)"/>
      <rect x="8" y="185" width="134" height="8" fill="#3a3a40"/>
      <rect x="8" y="205" width="134" height="6" fill="#3a3a40"/>
    </svg>
    <div class="bottle-body">
      <p class="brand-name">Orvia Lune</p>
      <div class="label-frame">
        <div class="label-section headline"><span class="headline-top">Anti-Aging</span><br>Facial Serum</div>
        <div class="label-section descriptor">Hydrating &amp; Plumping Formula</div>
        <div class="label-section product"><p class="product-name product-name--long">Hyaluronic<br>Acid</p><p class="product-note">With Dead Sea Minerals</p></div>
        <div class="label-section volume">1.7 oz / 50 ml</div>
      </div>
    </div>
  </article>
</main>
</body>
</html>
```